Design Business Card & Logo for Lumi Tot

I need a BUSINESS CARD DESIGNED. The name of the company is Lumi Tot and we sell high end Childrens Clothing.

The colors I prefer to use are shades of blue and purple.

For the card the details are as follows
the name should be Zerina Khatib with the title Director, EMAIL zerina@lumitot.co.za
Social Link.
Facebook www.facebook.com/lumitot
Whatsapp: 0748815092
Instagram #lumitot

Two sided one Logo Only and One Side with the logo and info

I like geomatric shapes to be used in the card. (Not a Must)

Delivery of logo should be in a 300dpi photoshop file and for the card a PRINT ready file with margins,

and if you need any more details please ask.

Feel free to modify the current logo if you feel you have something better.

Thank you,

```html
<!DOCTYPE html>
<html lang="en">
<head>
<meta charset="utf-8">
<title>Lumi Tot – Business Card</title>
<link rel="stylesheet" href="https://fonts.googleapis.com/css2?family=Della+Respira&family=Delius&display=swap">
<style>
  :root {
    --backdrop: #ece6df;
    --ink-brown: #4a2a18;
    --magenta: #b0479c;
    --plum: #7a3f78;
    --steel-blue: #a9c1d1;
    --title-blue: #8eaabd;
    --contact-ink: #3a2a3a;
    --white: #ffffff;
    --back-light: #a6519a;
    --back-dark: #7c2070;
  }
  * { margin: 0; padding: 0; box-sizing: border-box; }
  html, body { width: 1200px; height: 851px; overflow: hidden; }
  body {
    position: relative;
    background: var(--backdrop);
    font-family: "Della Respira", serif;
  }
  .brand-mark {
    position: absolute;
    left: 67px;
    top: 323px;
    width: 350px;
    text-align: center;
  }
  .brand-mark .dot {
    display: block;
    width: 60px; height: 60px;
    margin: 0 auto 14px;
    border-radius: 50%;
    background: var(--ink-brown);
  }
  .brand-mark .wordmark {
    font-size: 58px;
    line-height: 1;
    color: var(--ink-brown);
  }
  .card {
    position: absolute;
    left: 437px;
    width: 588px;
    height: 327px;
    overflow: hidden;
    box-shadow: 0 3px 10px rgba(0,0,0,.18);
  }
  .card-front { top: 72px; background: var(--white); }
  .card-back {
    top: 443px;
    background: radial-gradient(ellipse at 50% 45%, var(--back-light) 0%, var(--back-dark) 85%);
    display: flex; flex-direction: column; align-items: center; justify-content: center;
  }
  .front-brand {
    position: absolute;
    left: 27px; top: 34px;
    width: 240px;
    text-align: center;
  }
  .front-brand .dot {
    display: block;
    width: 40px; height: 40px;
    margin: 0 auto 10px;
    border-radius: 50%;
    background: var(--steel-blue);
  }
  .front-brand .wordmark { font-size: 40px; line-height: 1; color: var(--plum); }
  .person { position: absolute; left: 352px; top: 84px; font-family: "Delius", sans-serif; }
  .person .name { font-size: 24px; color: var(--magenta); line-height: 1.2; }
  .person .role { font-size: 20px; color: var(--title-blue); line-height: 1.2; }
  .icon-tab {
    position: absolute;
    left: 0; top: 152px;
    width: 29px; height: 123px;
    background: var(--magenta);
    border-radius: 0 6px 6px 0;
  }
  .icon-tab svg { position: absolute; left: 7px; width: 15px; height: 15px; }
  .contact-list {
    position: absolute;
    left: 41px; top: 164px;
    list-style: none;
    font-size: 17px;
    color: var(--contact-ink);
  }
  .contact-list li { height: 23.5px; line-height: 23.5px; }
  .footer-bands { position: absolute; left: 0; bottom: 0; width: 588px; height: 31px; }
  .back-brand .dot {
    display: block;
    width: 48px; height: 48px;
    margin: 0 auto 16px;
    border-radius: 50%;
    background: var(--white);
  }
  .back-brand .wordmark { font-size: 48px; line-height: 1; color: var(--white); }
</style>
</head>
<body>
  <div class="brand-mark">
    <span class="dot"></span>
    <div class="wordmark">Lumi Tot</div>
  </div>

  <section class="card card-front">
    <div class="front-brand">
      <span class="dot"></span>
      <div class="wordmark">Lumi Tot</div>
    </div>

    <div class="person">
      <div class="name">Zerina Khatib</div>
      <div class="role">Director</div>
    </div>

    <div class="icon-tab">
      <svg style="top:19px" viewBox="0 0 16 16"><rect x="1" y="3" width="14" height="10" rx="1" fill="#fff"/><path d="M1.5 3.5 L8 9 L14.5 3.5" stroke="#b0479c" stroke-width="1.4" fill="none"/></svg>
      <svg style="top:43px" viewBox="0 0 16 16"><path d="M4 1.5 L6.5 1.5 L7.5 5 L5.8 6.3 Q7 9 9.7 10.2 L11 8.5 L14.5 9.5 L14.5 12 Q14.5 14.5 12 14.5 Q2 13.5 1.5 4 Q1.5 1.5 4 1.5Z" fill="#fff"/></svg>
      <svg style="top:66px" viewBox="0 0 16 16"><rect x="2" y="2" width="12" height="12" rx="2" fill="#fff"/></svg>
      <svg style="top:90px" viewBox="0 0 16 16"><rect x="2" y="2" width="12" height="12" fill="#fff"/></svg>
    </div>

    <ul class="contact-list">
      <li>zerina@lumitot.co.za</li>
      <li>0748815092</li>
      <li>#lumitot</li>
      <li>/lumitot</li>
    </ul>

    <svg class="footer-bands" viewBox="0 0 588 31" preserveAspectRatio="none">
      <polygon points="0,0 313,0 337,31 0,31" fill="var(--magenta)"/>
      <polygon points="318,4 588,4 588,31 342,31" fill="var(--steel-blue)"/>
    </svg>
  </section>

  <section class="card card-back">
    <div class="back-brand">
      <span class="dot"></span>
      <div class="wordmark">Lumi Tot</div>
    </div>
  </section>
</body>
</html>
```